BANNER PUBBLICITARIO FACEBOOK

Advertise our services via facebook.
We are a medical center of diagnostic imaging, perform MRI, CT, ultrasound and specialist visits. I want to advertise our center through Facebook trying to get the knowledge of our center to as many people as possible. our target audience are people from 18 to 80 years old.
I want to highlight our contact details, our address and our website www. ponteval.it. All contact information can be found on our website
Updates

Target Market(s)

my target market are people from 18 to 80 years old who have to perform diagnostic tests such as magnetic resonance imaging tac ultrasound etc

Colors
0054AA
0677BA
7BADD7
CADEEF
E8F1F8
0094D4
00A9DD
6FCCEA
C7EBF8
E9F6FB
00AB8E
00BBA5
67D7C9
C6EFE9
E9F9F6

Requirements
Must have
• my project should be impactful and attractive. When the user sees my post he must be attracted
Nice to have
• I would like to highlight our diagnostic machines, so that the customers understand immediately what we are doing. As indicated on our website www.ponteval.it

```html
<!DOCTYPE html>
<html lang="en">
<head>
<meta charset="utf-8">
<title>Ponteval – Diagnostic Imaging Ads</title>
<link rel="stylesheet" href="https://fonts.googleapis.com/css2?family=Montserrat:wght@400;500;600&family=Open+Sans:wght@700;800&family=Lato:wght@400;700&display=swap">
<style>
:root{
  --board:#363539;
  --blue:#1f74bf;
  --blue-deep:#0054AA;
  --teal:#00A896;
  --teal-light:#67D7C9;
  --grey-band:#eeefef;
  --white:#ffffff;
  --photo-a:#9fb6c9;
  --photo-b:#c9d3da;
  --photo-c:#6f8aa3;
}
*{margin:0;padding:0;box-sizing:border-box}
html,body{width:951px;height:1200px;overflow:hidden;background:var(--board)}
.board{position:relative;width:951px;height:1200px;background:var(--board);font-family:'Lato',sans-serif}
.board-label{position:absolute;left:0;width:951px;text-align:center;color:#e8e8e8;font-family:'Montserrat',sans-serif;font-size:15px;letter-spacing:.5px}
.card{position:absolute;background:var(--white);overflow:hidden;box-shadow:0 4px 10px rgba(0,0,0,.35)}
.card svg.art{position:absolute;left:0;top:0}
.abs{position:absolute}
.brand{display:flex;align-items:center;gap:8px;color:var(--blue);font-family:'Montserrat',sans-serif;font-weight:600}
.brand-dot{border-radius:50%;background:var(--teal)}
.kicker{font-family:'Montserrat',sans-serif;color:var(--teal);white-space:nowrap}
.headline{font-family:'Open Sans',sans-serif;font-weight:800;color:var(--blue);white-space:nowrap;line-height:1}
.contact{display:flex;align-items:center;color:var(--white);line-height:1.25}
.contact-icon{background:var(--white);border-radius:4px;display:flex;align-items:center;justify-content:center;flex:none}
.service-strip{color:var(--white);font-size:16px;display:flex;gap:14px;white-space:nowrap;align-items:center}
.service-strip span{display:flex;align-items:center;gap:4px}
.service-row{position:absolute;display:flex;align-items:center;gap:6px;padding-left:0;font-size:20px;white-space:nowrap}
.service-row.on-blue{color:var(--white)}
.service-row.on-grey{color:#555}
</style>
</head>
<body>
<div class="board">

  <div class="board-label" style="top:79px">Ad Banner</div>

  <!-- Wide ad banner -->
  <section class="card banner" style="left:75px;top:112px;width:802px;height:240px">
    <svg class="art" width="802" height="240" viewBox="0 0 802 240">
      <polygon points="0,17 182,17 160,69 0,69" fill="var(--grey-band)"/>
      <polygon points="186,17 198,17 176,69 164,69" fill="var(--blue)"/>
      <polygon points="204,17 216,17 194,69 182,69" fill="var(--teal)"/>
      <rect x="345" y="17" width="105" height="144" rx="6" fill="#d9dde2" role="img" aria-label="Ultrasound diagnostic machine"/>
      <polygon points="0,162 465,162 460,191 0,191" fill="var(--teal)"/>
      <polygon points="0,191 460,191 480,140 535,240 0,240" fill="var(--blue)"/>
      <polygon points="486,0 802,0 802,168 605,170 581,58 532,216" fill="url(#bannerPhoto)" role="img" aria-label="Doctor performing an abdominal ultrasound on a patient"/>
      <defs>
        <linearGradient id="bannerPhoto" x1="0" y1="0" x2="1" y2="1">
          <stop offset="0" stop-color="var(--photo-a)"/>
          <stop offset="1" stop-color="var(--photo-c)"/>
        </linearGradient>
      </defs>
      <polyline points="446,200 480,2 532,218 581,56 603,180 785,180" fill="none" stroke="var(--teal)" stroke-width="14" stroke-linejoin="miter"/>
      <circle cx="790" cy="181" r="20" fill="var(--teal)"/>
      <circle cx="647" cy="180" r="44" fill="var(--white)"/>
      <circle cx="647" cy="180" r="40" fill="none" stroke="var(--blue)" stroke-width="3"/>
      <circle cx="647" cy="180" r="36" fill="var(--photo-b)" role="img" aria-label="Doctor with patient at a CT scanner"/>
      <circle cx="747" cy="182" r="36" fill="var(--white)"/>
      <circle cx="747" cy="182" r="33" fill="none" stroke="var(--blue)" stroke-width="3"/>
      <circle cx="747" cy="182" r="29" fill="#a9d3de" role="img" aria-label="Doctor with digital health interface"/>
    </svg>

    <div class="abs brand" style="left:19px;top:28px;font-size:22px">
      <span>Ponteval</span><span class="brand-dot" style="width:9px;height:9px"></span>
    </div>
    <div class="abs kicker" style="left:25px;top:83px;font-size:25px">Medical Center Of</div>
    <div class="abs headline" style="left:22px;top:113px;font-size:34px">Diagnostic Imaging</div>

    <div class="abs service-strip" style="left:26px;top:165px">
      <span><svg width="12" height="12" viewBox="0 0 12 12"><circle cx="6" cy="6" r="5" fill="none" stroke="#fff" stroke-width="1.2"/><path d="M3.5 6l2 2 4-5" fill="none" stroke="#fff" stroke-width="1.3"/></svg>Perform MRI</span>
      <span><svg width="12" height="12" viewBox="0 0 12 12"><circle cx="6" cy="6" r="5" fill="none" stroke="#fff" stroke-width="1.2"/><path d="M3.5 6l2 2 4-5" fill="none" stroke="#fff" stroke-width="1.3"/></svg>CT</span>
      <span><svg width="12" height="12" viewBox="0 0 12 12"><circle cx="6" cy="6" r="5" fill="none" stroke="#fff" stroke-width="1.2"/><path d="M3.5 6l2 2 4-5" fill="none" stroke="#fff" stroke-width="1.3"/></svg>Ultrasound and specialist visits</span>
    </div>

    <div class="abs contact" style="left:27px;top:205px;font-size:10px;gap:8px">
      <span class="contact-icon" style="width:21px;height:21px"><svg width="12" height="14" viewBox="0 0 12 14"><path d="M6 0a5 5 0 0 0-5 5c0 4 5 9 5 9s5-5 5-9a5 5 0 0 0-5-5z" fill="var(--blue)"/><circle cx="6" cy="5" r="2" fill="#fff"/></svg></span>
      <span>Via dei Tigli, 18<br>47890 Serravalle (RSM)</span>
    </div>
    <div class="abs contact" style="left:188px;top:205px;font-size:10px;gap:8px">
      <span class="contact-icon" style="width:21px;height:21px"><svg width="13" height="13" viewBox="0 0 13 13"><path d="M3 0l2 3-1.5 1.5a8 8 0 0 0 5 5L10 8l3 2-1.5 3C6 13 0 7 0 1.5z" fill="var(--blue)"/></svg></span>
      <span>0549 00 12 34<br>351 00 222 33</span>
    </div>
    <div class="abs contact" style="left:318px;top:205px;font-size:10px;gap:8px">
      <span class="contact-icon" style="width:21px;height:21px"><svg width="14" height="14" viewBox="0 0 14 14"><circle cx="7" cy="7" r="6" fill="none" stroke="var(--blue)" stroke-width="1.5"/><path d="M1 7h12M7 1c-3 3-3 9 0 12M7 1c3 3 3 9 0 12" fill="none" stroke="var(--blue)" stroke-width="1.2"/></svg></span>
      <span>info@ponteval.it<br>www.ponteval.it</span>
    </div>
  </section>

  <div class="board-label" style="top:400px">Facebook Post</div>

  <!-- Square social post -->
  <section class="card post" style="left:148px;top:433px;width:655px;height:655px">
    <svg class="art" width="655" height="655" viewBox="0 0 655 655">
      <defs>
        <linearGradient id="postPhoto" x1="0" y1="0" x2="1" y2="1">
          <stop offset="0" stop-color="var(--photo-a)"/>
          <stop offset="1" stop-color="var(--photo-c)"/>
        </linearGradient>
      </defs>
      <polygon points="0,37 321,37 308,112 0,112" fill="var(--grey-band)"/>
      <polygon points="361,0 655,0 655,318 564,268 525,101 436,402 353,104" fill="url(#postPhoto)" role="img" aria-label="Doctor performing an abdominal ultrasound on a patient"/>
      <polyline points="0,279 22,279" fill="none" stroke="var(--teal)" stroke-width="24"/>
      <polyline points="280,279 294,279 347,-4 434,519 525,96 564,268" fill="none" stroke="var(--teal)" stroke-width="22" stroke-linejoin="miter"/>
      <polyline points="610,335 655,335" fill="none" stroke="var(--teal)" stroke-width="24"/>
      <circle cx="150" cy="259" r="121" fill="var(--white)"/>
      <circle cx="150" cy="259" r="115" fill="none" stroke="var(--blue)" stroke-width="10"/>
      <circle cx="150" cy="259" r="105" fill="var(--photo-b)" role="img" aria-label="Radiologist with a patient at a CT scanner"/>
      <circle cx="568" cy="338" r="66" fill="var(--white)"/>
      <circle cx="568" cy="338" r="62" fill="none" stroke="var(--blue)" stroke-width="4"/>
      <circle cx="568" cy="338" r="56" fill="#a9d3de" role="img" aria-label="Doctor with digital health interface"/>
      <polygon points="482,417 655,417 655,445 472,445" fill="var(--blue)"/>
      <polygon points="472,453 655,453 655,481 462,481" fill="var(--grey-band)"/>
      <polygon points="462,489 655,489 655,517 451,517" fill="var(--blue)"/>
      <polygon points="451,526 655,526 655,554 440,554" fill="var(--grey-band)"/>
      <rect x="0" y="570" width="655" height="53" fill="var(--blue)"/>
    </svg>

    <div class="abs brand" style="left:44px;top:55px;font-size:38px">
      <span>Ponteval</span><span class="brand-dot" style="width:14px;height:14px"></span>
    </div>

    <div class="abs kicker" style="left:37px;top:394px;font-size:24px;font-weight:500">Medical Center Of</div>
    <div class="abs headline" style="left:32px;top:428px;font-size:63px">Diagnostic</div>
    <div class="abs headline" style="left:32px;top:494px;font-size:63px">Imaging</div>

    <div class="service-row on-blue" style="left:484px;top:418px">
      <svg width="14" height="14" viewBox="0 0 14 14"><circle cx="7" cy="7" r="5.5" fill="none" stroke="#fff" stroke-width="1.5"/><path d="M4 7l2.2 2.2L10.5 4" fill="none" stroke="var(--teal-light)" stroke-width="1.5"/></svg>Perform MRI</div>
    <div class="service-row on-grey" style="left:484px;top:454px">
      <svg width="14" height="14" viewBox="0 0 14 14"><circle cx="7" cy="7" r="5.5" fill="none" stroke="var(--blue)" stroke-width="1.5"/><path d="M4 7l2.2 2.2L10.5 4" fill="none" stroke="var(--teal)" stroke-width="1.5"/></svg>CT</div>
    <div class="service-row on-blue" style="left:484px;top:490px">
      <svg width="14" height="14" viewBox="0 0 14 14"><circle cx="7" cy="7" r="5.5" fill="none" stroke="#fff" stroke-width="1.5"/><path d="M4 7l2.2 2.2L10.5 4" fill="none" stroke="var(--teal-light)" stroke-width="1.5"/></svg>Ultrasound</div>
    <div class="service-row on-grey" style="left:484px;top:527px">
      <svg width="14" height="14" viewBox="0 0 14 14"><circle cx="7" cy="7" r="5.5" fill="none" stroke="var(--blue)" stroke-width="1.5"/><path d="M4 7l2.2 2.2L10.5 4" fill="none" stroke="var(--teal)" stroke-width="1.5"/></svg>Specialist visits</div>

    <div class="abs contact" style="left:44px;top:580px;font-size:14px;gap:10px">
      <span class="contact-icon" style="width:30px;height:30px"><svg width="16" height="20" viewBox="0 0 12 14"><path d="M6 0a5 5 0 0 0-5 5c0 4 5 9 5 9s5-5 5-9a5 5 0 0 0-5-5z" fill="var(--blue)"/><circle cx="6" cy="5" r="2" fill="#fff"/></svg></span>
      <span>Via dei Tigli, 18<br>47890 Serravalle (RSM)</span>
    </div>
    <div class="abs contact" style="left:270px;top:580px;font-size:14px;gap:10px">
      <span class="contact-icon" style="width:30px;height:30px"><svg width="18" height="18" viewBox="0 0 13 13"><path d="M3 0l2 3-1.5 1.5a8 8 0 0 0 5 5L10 8l3 2-1.5 3C6 13 0 7 0 1.5z" fill="var(--blue)"/></svg></span>
      <span>0549 00 12 34<br>351 00 222 33</span>
    </div>
    <div class="abs contact" style="left:452px;top:580px;font-size:14px;gap:12px">
      <span class="contact-icon" style="width:30px;height:30px"><svg width="20" height="20" viewBox="0 0 14 14"><circle cx="7" cy="7" r="6" fill="none" stroke="var(--blue)" stroke-width="1.5"/><path d="M1 7h12M7 1c-3 3-3 9 0 12M7 1c3 3 3 9 0 12" fill="none" stroke="var(--blue)" stroke-width="1.2"/></svg></span>
      <span>info@ponteval.it<br>www.ponteval.it</span>
    </div>
  </section>

</div>
</body>
</html>
```